Harvest Bridge Christian Ministry needs a Conference Ad

We are a Christian nonprofit focused on eliminating systemic poverty and helping believers function as ministers in their workplaces. The 2025 Lantern Path Global Conference coming up in October, and we need an ad for social media (facebook, instagram, and X) and our website in order to get people excited to attend! We are looking for a modern and sleek design that incorporates our logo (attached file). You can either put just the butterfly and then write our company name separately somewhere in the design or use it as is (we used Gotham font for the logo). We want to emphasize the joy of in-person connection at the conference, so you could possibly include stock photos of young people gathering together. You could also include the attached photo of our founders in the design and say “with Mel and Dora Quintavan". Also, include the conference dates, which are October 9-12, 2025, and say “come in person or join online”. Lastly, please include the tagline “from the Pellmore Awakening to Worldwide Transformation”. NOTE: I’m attaching AN EXAMPLE I’ve created of how the design could look, which you can feel free to use for inspiration.
Young people on Instagram and facebook
- Gotham

```html
<!DOCTYPE html>
<html lang="en">
<head>
<meta charset="utf-8">
<title>Lantern Path Global Conference 2025</title>
<link rel="stylesheet" href="https://fonts.googleapis.com/css2?family=Montserrat:wght@500;600;700&display=swap">
<style>
  :root {
    --teal-deep: #285a75;
    --teal-light: #3a88ab;
    --navy-tint: #2c4a78;
    --navy-dark: #0a1226;
    --navy-pill: #0b1834;
    --sky: #7fdcf6;
    --mint: #2ee58a;
    --lemon: #f2f57a;
    --gold: #f5c800;
    --white: #ffffff;
  }
  * { margin: 0; padding: 0; box-sizing: border-box; }
  html, body { width: 1200px; height: 1006px; overflow: hidden; background: var(--teal-deep); }
  .ad {
    position: relative;
    width: 1200px;
    height: 1006px;
    overflow: hidden;
    font-family: "Montserrat", sans-serif;
    background: var(--teal-deep);
  }
  .backdrop { position: absolute; inset: 0; }
  .crowd-photo {
    position: absolute;
    left: 47px; top: 48px;
    width: 486px; height: 486px;
    border-radius: 50%;
    border: 7px solid var(--white);
    background: radial-gradient(circle at 45% 40%, #e9dccd 0%, #b88a64 40%, #7a4a36 70%, #5a2a2a 100%);
  }
  .info { position: absolute; left: 557px; width: 603px; text-align: center; white-space: nowrap; font-weight: 700; line-height: 1; }
  .brand-name { top: 62px; color: var(--white); font-size: 32px; letter-spacing: 3px; }
  .title-one { top: 118px; color: var(--sky); font-size: 84px; letter-spacing: 2px; }
  .title-two { top: 212px; color: var(--mint); font-size: 84px; letter-spacing: 2px; }
  .subtitle { top: 312px; color: var(--white); font-size: 44px; letter-spacing: 1px; }
  .year-row {
    position: absolute;
    left: 557px; top: 370px;
    width: 603px;
    display: flex;
    align-items: center;
    gap: 10px;
  }
  .year-row .rule { flex: 1; height: 4px; background: var(--lemon); }
  .year-row .year { font-weight: 700; font-size: 46px; color: var(--gold); line-height: 1; }
  .dates { top: 432px; color: var(--white); font-size: 26px; letter-spacing: 1px; }
  .attend { top: 468px; color: var(--lemon); font-size: 18px; font-weight: 600; letter-spacing: 1px; }
  .headline-panel {
    position: absolute;
    left: 0; top: 578px;
    width: 660px; height: 302px;
    background: var(--navy-dark);
  }
  .headline {
    position: absolute;
    left: 29px; top: 600px;
    color: var(--white);
    font-weight: 600;
    font-size: 76px;
    line-height: 88px;
    letter-spacing: 1px;
  }
  .tagline {
    position: absolute;
    left: 29px; top: 896px;
    color: var(--white);
    font-weight: 600;
    font-size: 14px;
    letter-spacing: 0.3px;
    white-space: nowrap;
  }
  .founders-photo {
    position: absolute;
    left: 614px; top: 508px;
    width: 586px; height: 498px;
    border-radius: 240px 240px 0 0;
    background: linear-gradient(160deg, #e6b87a 0%, #c99a74 30%, #1c2030 60%, #0f1320 100%);
  }
  .host-pill {
    position: absolute;
    left: 174px; top: 926px;
    width: 517px; height: 57px;
    border-radius: 28px;
    background: var(--navy-pill);
    color: var(--white);
    display: flex;
    align-items: center;
    justify-content: center;
    font-weight: 500;
    font-size: 24px;
    letter-spacing: 0.5px;
  }
</style>
</head>
<body>
  <main class="ad">
    <svg class="backdrop" width="1200" height="1006" viewBox="0 0 1200 1006" aria-hidden="true">
      <rect width="1200" height="1006" fill="var(--teal-deep)"/>
      <polygon points="0,1006 0,560 1200,330 1200,1006" fill="var(--teal-light)"/>
      <polygon points="0,470 760,0 1200,0 1200,350 610,580 0,580" fill="var(--navy-tint)"/>
      <polygon points="0,880 330,880 0,1006" fill="var(--navy-tint)"/>
    </svg>

    <div class="crowd-photo" role="img" aria-label="Photo of young friends laughing and embracing at a gathering"></div>

    <div class="info brand-name">HARVEST BRIDGE</div>

    <h1>
      <span class="info title-one">LANTERN</span>
      <span class="info title-two">PATH</span>
      <span class="info subtitle">GLOBAL CONFERENCE</span>
    </h1>
    <div class="year-row"><span class="rule"></span><span class="year">2025</span></div>
    <p class="info dates">OCTOBER 9–12, 2025</p>
    <p class="info attend">COME IN PERSON OR JOIN ONLINE</p>

    <div class="headline-panel"></div>
    <h2 class="headline">TRANSFORM<br>HAPPENS<br>TOGETHER</h2>
    <p class="tagline">FROM THE PELLMORE AWAKENING TO WORLDWIDE TRANSFORMATION</p>

    <div class="founders-photo" role="img" aria-label="Photo of the founders Mel and Dora Quintavan smiling together"></div>

    <p class="host-pill">WITH MEL AND DORA QUINTAVAN</p>
  </main>
</body>
</html>
```